Bluestone Nine LLC Flyer Design

Marketing Materials for Real Estate Company. This flyer will be used to promote the company throughout the Commercial Real Estate business in the United States. The team has been together for 15 years. We are the middle guys between the Tenant, Broker, and the Owner. In the case of working with a Franchisor, we will be their Plug and Play leasing arm that will assist their new Franchisee's with their site selection, lease negotiations, design and construction management.

Target Market(s)

Real Estate Owners, Franchisor's, and Brokers

Font styles to use
Serif

Colors

Designer to choose colors to be used in the design.

Requirements
Must have
• The flyer must have......
• 1. The Best Leasing Machine On The Planet
• 2. Over the past 15 years our group has completed 4,492 lease transactions resulting in leasing 17,803,114 square feet in shopping centers across the United States.
• 3. Plug and Play Leasing Specialists. We handle the details between when the broker shows up with the space and the tenant and completing the lease negotiations, legal negotiations and documentation, and construction management to Certificate of Occupancy.
• 4. For Information Call Colette Varga at 555-014-2763 or Wendy Falk at 555-017-8302.
Nice to have
• National Tenants the we have completed transactions with....
• Pellmart, Fresh Basket, Harbor Pams, Vexo, Dunn, QV Rendo, Burrasco, Pattersons, Wrap Shack, Brewhorns, Summit Workout, ShipVo, Tredwell, PKN, Halvorsons, Q&L, Ledger Union Bank, Hen Haus-O, Lotus Kitchen, Furvo, Dex-Mart, Fieldly, and Orbit Theaters

```html
<!DOCTYPE html>
<html lang="en">
<head>
<meta charset="utf-8">
<title>Bluestone Nine LLC – Leasing Flyer</title>
<link rel="stylesheet" href="https://fonts.googleapis.com/css2?family=Merriweather:wght@400;700;900&family=Quicksand:wght@600&family=Lato:wght@400&display=swap">
<style>
  :root {
    --brand-green: #8aa63c;
    --ink: #3a3a3a;
    --heading-ink: #444444;
    --muted: #8a8a8a;
    --rule: #dedede;
    --footer-slate: #7a898d;
    --paper: #ffffff;
    --white: #ffffff;
  }
  * { margin: 0; padding: 0; box-sizing: border-box; }
  html, body { width: 848px; height: 1200px; overflow: hidden; background: var(--paper); }
  .flyer { position: relative; width: 848px; height: 1200px; overflow: hidden; background: var(--paper); }

  .brand-name {
    position: absolute; left: 40px; top: 30px;
    font-family: "Quicksand", sans-serif; font-weight: 600;
    font-size: 31px; letter-spacing: 1px; color: var(--brand-green);
  }

  .hero-photo {
    position: absolute; left: 0; top: 103px; width: 848px; height: 450px;
    background: linear-gradient(180deg, #4a97dc 0%, #8cc0ea 38%, #6e5a4c 55%, #7c6a58 68%, #d9d6cc 84%, #b9a878 100%);
  }

  .headline-panel {
    position: absolute; left: 0; top: 449px; width: 425px; height: 143px;
    background: var(--brand-green);
    display: flex; align-items: center; padding-left: 30px;
  }
  .headline {
    font-family: "Merriweather", serif; font-weight: 700;
    font-size: 29px; line-height: 1.4; color: var(--white);
  }

  .about-heading {
    position: absolute; left: 51px; top: 628px;
    font-family: "Merriweather", serif; font-weight: 700;
    font-size: 20px; letter-spacing: 1.5px; color: var(--heading-ink);
  }
  .about-text {
    position: absolute; top: 670px;
    font-family: "Merriweather", serif; font-weight: 400;
    font-size: 17.5px; line-height: 30px; color: var(--ink);
  }
  .about-text.stats { left: 51px; width: 365px; }
  .about-text.services { left: 425px; width: 375px; }
  .stat { font-weight: 900; font-size: 22px; }

  .divider {
    position: absolute; left: 31px; top: 873px; width: 762px; height: 1px;
    background: var(--rule);
  }

  .tenants {
    position: absolute; left: 54px; top: 912px; width: 740px; text-align: center;
  }
  .tenants-intro {
    font-family: "Lato", sans-serif; font-size: 17px; color: var(--muted);
    margin-bottom: 8px;
  }
  .tenants-list {
    font-family: "Merriweather", serif; font-weight: 700;
    font-size: 18px; line-height: 31px; color: var(--ink);
  }

  .contact-band {
    position: absolute; left: 0; top: 1083px; width: 848px; height: 117px;
    background: var(--footer-slate);
    display: flex; align-items: center; justify-content: center; text-align: center;
  }
  .contact-text {
    font-family: "Merriweather", serif; font-weight: 700;
    font-size: 21px; line-height: 35px; color: var(--white);
  }
</style>
</head>
<body>
  <main class="flyer">
    <div class="brand-name">Bluestone Nine LLC</div>

    <div class="hero-photo" role="img" aria-label="Photograph of a large brick and stone suburban house with gabled roofs, a wide driveway and bare trees under a clear blue sky"></div>

    <div class="headline-panel">
      <h1 class="headline">The Best Leasing<br>Machine On The Planet</h1>
    </div>

    <h2 class="about-heading">ABOUT US</h2>

    <p class="about-text stats">Over the past <span class="stat">15 years</span> our group has completed <span class="stat">4,492 lease</span> transactions resulting in leasing <span class="stat">17,803,114 square feet</span> in shopping centers across the United States.</p>

    <p class="about-text services">Plug and Play Leasing Specialists. We handle the details between when the broker shows up with the space and the tenant and com&shy;pleting the lease negotiations, legal negotia&shy;tions and documentation, and construction management to Certificate of Occupancy.</p>

    <div class="divider"></div>

    <section class="tenants">
      <p class="tenants-intro">National Tenants the we have completed transactions with</p>
      <p class="tenants-list">Pellmart, Fresh Basket, Harbor Pams, Vexo, Dunn, QV Rendo, Burrasco, Pattersons, Wrap Shack, Brewhorns, Summit Workout, ShipVo, Tredwell, PKN, Halvorsons, Q&amp;L, Ledger Union Bank, Hen Haus-O, Lotus Kitchen, Furvo, Dex-Mart, Fieldly, and Orbit Theaters</p>
    </section>

    <footer class="contact-band">
      <p class="contact-text">For Information Call&nbsp; Colette Varga at 555-014-2763 or<br>Wendy Falk at 555-017-8302.</p>
    </footer>
  </main>
</body>
</html>
```